Tidewell Hypnotherapy 2017 DL Card Flyer

We would like a double sided DL Card Flyer design.

We are a professional Hypnotherapy Clinic looking for a fresh clean design.

Front of card is summary info and back of flyer is detailed text.

I have attached documents with text for the front (dl size hypno 1) and back (dl size hypno 2) of the card and an indicative style of layout.

There are logo files uploaded as well as one image file.

The colors we like are blue, white and yellow/gold.
Updates

please note: when using the 'bright steps bold change' image, please only use the top half of the image. The girl is not to be in the image, just the words and light bulb with the chalk underline. thanks.. Added Sunday, March 19, 2017

Industry/Entity Type

Health And Wellness

Requirements
Must have
• Note. I have misspelled the www.TidewellHypnotherapy.com.au (missing an 'o' in the attachments to the brief). My error. Please amend in your design submissions.

```html
<!DOCTYPE html>
<html lang="en">
<head>
<meta charset="utf-8">
<title>Tidewell Hypnotherapy – Banner Front and Back</title>
<link href="https://fonts.googleapis.com/css2?family=Titillium+Web:wght@300;400;600;700&display=swap" rel="stylesheet">
<style>
  :root {
    --navy: #262f7a;
    --blue: #2b3d92;
    --blue-light: #4a5fb8;
    --grey: #8e9199;
    --grey-dark: #5e6168;
    --panel: #eef0f2;
    --panel-edge: #e2e5e8;
    --stage: #d8d9db;
    --ink: #2b2b30;
    --white: #ffffff;
    --board: #3a3c3f;
    --gold: #f3d64a;
  }
  * { box-sizing: border-box; margin: 0; padding: 0; }
  html, body { width: 1200px; height: 1200px; overflow: hidden; }
  body {
    background: var(--stage);
    font-family: "Titillium Web", sans-serif;
    color: var(--ink);
    position: relative;
  }
  .panel {
    position: absolute;
    top: 120px;
    width: 430px;
    height: 960px;
    background: linear-gradient(160deg, #f6f7f8 0%, var(--panel) 55%, var(--panel-edge) 100%);
    overflow: hidden;
    display: flex;
    flex-direction: column;
  }
  .panel--front { left: 90px; }
  .panel--back { left: 680px; }

  .rule-top { height: 10px; background: var(--navy); margin-top: 6px; flex: none; }
  .rule-bottom { height: 14px; background: var(--navy); margin-top: 6px; flex: none; }

  /* brand */
  .brand { display: flex; align-items: center; justify-content: center; gap: 14px; flex: none; }
  .brand__dot { border-radius: 50%; background: var(--navy); flex: none; }
  .brand__name { font-weight: 700; color: var(--navy); line-height: 1; }
  .brand--front { height: 166px; }
  .brand--front .brand__dot { width: 86px; height: 86px; }
  .brand--front .brand__name { font-size: 32px; }
  .brand--back { height: 104px; gap: 10px; }
  .brand--back .brand__dot { width: 50px; height: 50px; }
  .brand--back .brand__name { font-size: 20px; }

  .divider { height: 5px; background: var(--navy); flex: none; }

  .hero-image {
    height: 180px;
    flex: none;
    margin-top: 6px;
    background: radial-gradient(circle at 50% 40%, #8a835a 0%, #4b4c4a 28%, var(--board) 70%);
  }

  .tagline {
    position: relative;
    height: 104px;
    flex: none;
    background: var(--blue);
    color: var(--white);
    display: flex;
    flex-direction: column;
    justify-content: center;
    padding-left: 74px;
  }
  .tagline svg { position: absolute; left: 0; top: 0; }
  .tagline__lead { font-size: 31px; font-weight: 600; line-height: 1.1; position: relative; }
  .tagline__rest { font-size: 27px; font-weight: 400; line-height: 1.2; position: relative; }

  .programs-title {
    text-align: center;
    font-size: 19px;
    font-weight: 700;
    color: var(--navy);
    margin: 18px 0 30px;
    flex: none;
  }
  .program-grid { flex: 1; display: flex; flex-direction: column; gap: 36px; }
  .program-row { display: flex; justify-content: center; }
  .program {
    width: 136px;
    display: flex; flex-direction: column; align-items: center;
    text-align: center;
    font-size: 13.5px; line-height: 1.2; color: var(--ink);
  }
  .program-row--two .program { width: 150px; }
  .program + .program { border-left: 1px solid #dadde0; }
  .icon-ring {
    width: 58px; height: 58px; border-radius: 50%;
    border: 2.5px solid var(--navy);
    background: var(--white);
    margin-bottom: 12px;
    display: flex; align-items: center; justify-content: center;
  }
  .icon-ring span { width: 30px; height: 30px; border-radius: 50%; background: #cfd4e6; }

  .contact {
    height: 118px; flex: none;
    background: var(--grey);
    display: flex; flex-direction: column; align-items: center; justify-content: center;
  }
  .contact__phone { display: flex; align-items: center; gap: 12px; color: var(--white); font-size: 42px; font-weight: 300; line-height: 1; }
  .contact__web { font-size: 19px; font-weight: 700; color: var(--navy); margin-top: 10px; }

  /* back */
  .detail-list { display: flex; flex-direction: column; gap: 9px; padding: 0 12px; flex: 1; }
  .detail {
    border: 1px solid #a8acb4;
    border-radius: 8px;
    background: rgba(255,255,255,0.35);
    padding-bottom: 5px;
  }
  .detail__head {
    position: relative;
    height: 22px;
    margin-top: 10px;
    background: var(--navy);
    color: var(--white);
    font-size: 11.5px;
    line-height: 22px;
    padding-left: 70px;
  }
  .detail__icon {
    position: absolute; left: 16px; top: -11px;
    width: 36px; height: 36px; border-radius: 50%;
    background: var(--white); border: 2px solid var(--navy);
  }
  .detail__body { padding: 4px 10px 0; font-size: 10.6px; line-height: 1.22; text-align: justify; }
  .detail__body p { margin-bottom: 7px; }
  .detail__sessions { font-weight: 600; }

  .back-footer {
    height: 80px; flex: none; margin: 14px 3px 0;
    background: var(--grey);
    display: flex; flex-direction: column; align-items: center; justify-content: center;
    text-align: center;
  }
  .back-footer__note { color: var(--white); font-size: 11.5px; line-height: 1.3; font-weight: 300; padding: 0 24px; }
  .back-footer__web { color: var(--white); font-size: 17px; font-weight: 700; margin-top: 6px; }
</style>
</head>
<body>

<section class="panel panel--front" aria-label="Banner front">
  <div class="rule-top"></div>
  <header class="brand brand--front">
    <span class="brand__dot"></span>
    <span class="brand__name">Tidewell Hypnotherapy</span>
  </header>
  <div class="divider"></div>
  <div class="hero-image" role="img" aria-label="Chalkboard photo with a glowing light bulb and the chalk words bright steps bold change"></div>
  <div class="tagline">
    <svg width="110" height="104" viewBox="0 0 110 104" aria-hidden="true">
      <polygon points="0,0 80,0 0,70" fill="#22307e"/>
      <polygon points="0,104 40,50 70,104" fill="#4a5fb8"/>
      <polygon points="0,104 20,60 40,104" fill="#1e2a6e"/>
    </svg>
    <span class="tagline__lead">There is nothing more</span>
    <span class="tagline__rest">important than good health</span>
  </div>
  <h2 class="programs-title">Professional Hypnosis Therapy Programs:</h2>
  <div class="program-grid">
    <div class="program-row">
      <div class="program"><div class="icon-ring" role="img" aria-label="Scales icon"><span></span></div>Weight Loss<br>(Virtual Gastric Band)</div>
      <div class="program"><div class="icon-ring" role="img" aria-label="Wrapped sweet icon"><span></span></div>Sugar Addiction</div>
      <div class="program"><div class="icon-ring" role="img" aria-label="No smoking icon"><span></span></div>Quit Smoking</div>
    </div>
    <div class="program-row program-row--two">
      <div class="program"><div class="icon-ring" role="img" aria-label="Person in pain icon"><span></span></div>Chronic Fatigue &amp;<br>Chronic Pain Relief</div>
      <div class="program"><div class="icon-ring" role="img" aria-label="Relaxation icon"><span></span></div>Stress Relief &amp;<br>Deep Relaxation</div>
    </div>
  </div>
  <footer class="contact">
    <div class="contact__phone">
      <svg width="46" height="40" viewBox="0 0 46 40" aria-hidden="true">
        <path d="M3 14 C3 4 43 4 43 14 L43 18 L33 18 L33 12 L13 12 L13 18 L3 18 Z" fill="#fff"/>
        <path d="M10 20 L36 20 L42 38 L4 38 Z" fill="#fff"/>
        <circle cx="23" cy="29" r="6" fill="none" stroke="#8e9199" stroke-width="3"/>
      </svg>
      1300 555 018
    </div>
    <div class="contact__web">www.TidewellHypnotherapy.com.au</div>
  </footer>
  <div class="rule-bottom"></div>
</section>

<section class="panel panel--back" aria-label="Banner back">
  <div class="rule-top"></div>
  <header class="brand brand--back">
    <span class="brand__dot"></span>
    <span class="brand__name">Tidewell Hypnotherapy</span>
  </header>
  <div class="detail-list">
    <article class="detail">
      <div class="detail__head"><span class="detail__icon"></span>WEIGHT LOSS PROGRAM (Virtual Gastric Band)</div>
      <div class="detail__body">
        <p>Achieve long term weight loss without dieting. Whether it’s losing 3kg or 30kg, we’ll help you become the shape and size you want to be.</p>
        <p>Our Internationally Accredited Program is proven to be 95% effective in clinical trials.</p>
        <div class="detail__sessions">Number of Sessions: 6+</div>
      </div>
    </article>
    <article class="detail">
      <div class="detail__head"><span class="detail__icon"></span>SUGAR ADDICTION PROGRAM</div>
      <div class="detail__body">
        <p>Excess sugar intake can lead to obesity, Type 2 Diabetes and tooth decay. The habit of reaching for soft drinks, chocolate, sweets, cakes and biscuits can be hard to break.</p>
        <p>By rewiring your subconscious habits, our Program puts you back in control.</p>
        <div class="detail__sessions">Number of Sessions: 3+</div>
      </div>
    </article>
    <article class="detail">
      <div class="detail__head"><span class="detail__icon"></span>QUIT SMOKING PROGRAM</div>
      <div class="detail__body">
        <p>The facts speak for themselves. You are 10 times more likely to quit smoking for good using hypnotherapy.</p>
        <p>Expect to be a non smoker after completing the first session of our Program. (12 Month Guarantee)</p>
        <div class="detail__sessions">Number of Sessions: 2</div>
      </div>
    </article>
    <article class="detail">
      <div class="detail__head"><span class="detail__icon"></span>CHRONIC FATIGUE &amp; CHRONIC PAIN RELIEF PROGRAM</div>
      <div class="detail__body">
        <p>Chronic Fatigue, Fibromyalgia and Chronic Musculoskeletal Pain are diseases of modern living.</p>
        <p>The <strong>symptoms</strong> of fatigue and pain are very real, however the <strong>cause</strong> is usually emotional, and is generally hidden beyond our conscious awareness.</p>
        <p>Our Program comprises Education and Hypnosis to help you regain your health, your self esteem, your friends and your life, all in a manageable timeframe.</p>
        <div class="detail__sessions">Number of Sessions: 6+</div>
      </div>
    </article>
    <article class="detail">
      <div class="detail__head"><span class="detail__icon"></span>STRESS RELIEF &amp; DEEP RELAXATION PROGRAM</div>
      <div class="detail__body">
        <p>Our Program gently uncovers the true source of your stress, and helps you reconnect to a natural inner calm. We teach you self hypnosis so that you have the tools to continue your experience.</p>
        <div class="detail__sessions">Number of Sessions: 3+</div>
      </div>
    </article>
  </div>
  <footer class="back-footer">
    <p class="back-footer__note">All Programs include take home CD’s personally recorded by our therapists, using advanced hypnotic techniques.</p>
    <p class="back-footer__web">www.TidewellHypnotherapy.com.au</p>
  </footer>
  <div class="rule-bottom"></div>
</section>

</body>
</html>
```